Modern, Clean, Edgy & Fun Comedy Show Flyer

We need to a create a new flyer for the comedy show, Harbor Laugh Nights. The original version of the flyer is attached (file: Old flyer), as well as two versions of the logo.
- The text should be the same except now the show is Every First Wednesday and the next show is June 1.
- Remove the jerk shop logo
- Remove the picture of the man, and replace it with a photo of Dale (our host), the Audience, or something of your own design.
* pictures of Dale and the Audience is attached.
* We'd like to keep the same color palette and have also attached a color palette for reference

I have also attached 4 references of flyers that I like, that you can use to get an idea of the theme and aesthetic we are looking for.
* Files: Reference 1, Reference 2, Reference 3, Reference 4
Updates

Colors
3277b5
85acd3
0455a3
eaf1f7
cee9f5
ecf7fb
d5d5d5
e6e6e6

Requirements
Must have
• The harbor laugh nights logo attached
• The text as specified in the project description
• An option with Dale and without

```html
<!DOCTYPE html>
<html lang="en">
<head>
<meta charset="utf-8">
<title>Harbor Laugh Nights – Comedy Show Flyer</title>
<link rel="stylesheet" href="https://fonts.googleapis.com/css2?family=Anton&family=Bebas+Neue&family=Montserrat:wght@700&display=swap">
<style>
  :root {
    --page: #f4f5f6;
    --night: #2f3442;
    --ink: #2b2f3a;
    --white: #ffffff;
    --teal: #5fc2a6;
    --sky: #9fc6d3;
    --lavender: #a49ccf;
    --plum: #5a5582;
    --aqua: #80cdc8;
    --mist: #d6eef6;
    --frost: #e9f6fa;
  }
  * { margin: 0; padding: 0; box-sizing: border-box; }
  html, body { width: 1200px; height: 1200px; overflow: hidden; background: var(--page); }
  .flyer {
    position: absolute; left: 185px; top: 7px;
    width: 830px; height: 1172px;
    transform: scale(1.012); transform-origin: top left;
    overflow: hidden; background: var(--night);
  }
  .flyer-art { position: absolute; inset: 0; }
  .venue {
    position: absolute; left: 66px; top: 40px; width: 698px;
    font-family: "Montserrat", sans-serif; font-weight: 700; font-size: 21px;
    letter-spacing: 2.4px; color: var(--white); white-space: nowrap;
  }
  .venue-name { color: var(--teal); margin-right: 14px; }
  .rule { position: absolute; left: 66px; width: 698px; height: 2px; background: var(--white); opacity: .85; }
  .rule--top { top: 88px; }
  .rule--mid { top: 385px; }
  .show-name {
    position: absolute; left: 62px; top: 180px; width: 340px;
    font-family: "Bebas Neue", sans-serif; font-weight: 400; font-size: 64px; line-height: .95;
    color: var(--white); text-align: center;
  }
  .headline {
    position: absolute; right: 66px; top: 104px; text-align: right;
    font-family: "Anton", sans-serif; font-weight: 400; color: var(--white); line-height: 1;
  }
  .headline-top { display: block; font-size: 116px; letter-spacing: -1px; }
  .headline-bottom { display: block; font-size: 156px; letter-spacing: -2px; margin-top: -6px; }
  .lineup { position: absolute; left: 66px; top: 400px; width: 698px; height: 200px; }
  .lineup text { font-family: "Bebas Neue", sans-serif; font-size: 70px; }
  .f-teal { fill: var(--teal); }
  .f-sky { fill: var(--sky); }
  .f-lav { fill: var(--lavender); }
  .t-plum { color: var(--plum); }
  .t-ink { color: var(--ink); }
  .details {
    position: absolute; right: 66px; top: 680px; width: 300px; text-align: right;
    font-family: "Bebas Neue", sans-serif; line-height: .92;
  }
  .details-group { padding: 8px 0 12px; }
  .details-group + .details-group { border-top: 2px solid var(--ink); }
  .d-xl { display: block; font-size: 68px; }
  .d-lg { display: block; font-size: 60px; }
  .d-md { display: block; font-size: 46px; }
  .d-sm { display: block; font-size: 40px; }
  .d-xs { display: block; font-size: 36px; }
</style>
</head>
<body>
  <article class="flyer">
    <svg class="flyer-art" width="830" height="1172" viewBox="0 0 830 1172">
      <defs>
        <linearGradient id="crowd" x1="0" y1="0" x2="0" y2="1">
          <stop offset="0" stop-color="#3a3f4e"/>
          <stop offset=".6" stop-color="#2f3442"/>
          <stop offset="1" stop-color="#262a36"/>
        </linearGradient>
        <linearGradient id="host" x1="0" y1="0" x2="0" y2="1">
          <stop offset="0" stop-color="#5a3626"/>
          <stop offset="1" stop-color="#2e211c"/>
        </linearGradient>
      </defs>
      <rect width="830" height="1172" fill="url(#crowd)" role="img" aria-label="Black and white photo of a packed comedy club audience under a warehouse ceiling"/>
      <polygon points="0,1000 830,605 830,1172 0,1172" fill="var(--aqua)"/>
      <rect x="0" y="600" width="430" height="572" fill="url(#host)" role="img" aria-label="Photo of the host smiling and holding a microphone on stage"/>
      <polygon points="420,650 790,630 800,1172 420,1172" fill="var(--mist)"/>
      <polygon points="560,800 830,760 830,1172 500,1172" fill="var(--frost)"/>
    </svg>

    <p class="venue"><span class="venue-name">THE INK ROOM</span>42 LINDEN AVENUE HARBORSIDE</p>
    <div class="rule rule--top"></div>

    <h2 class="show-name">HARBOR LAUGH NIGHTS</h2>
    <h1 class="headline"><span class="headline-top">COMEDY</span><span class="headline-bottom">SHOW</span></h1>
    <div class="rule rule--mid"></div>

    <svg class="lineup" viewBox="0 0 698 200" aria-label="Line-up">
      <text x="0" y="62" textLength="698" lengthAdjust="spacingAndGlyphs"><tspan class="f-teal">FEATURING</tspan> <tspan class="f-sky">VICTOR HALE</tspan></text>
      <text x="0" y="126" textLength="698" lengthAdjust="spacingAndGlyphs"><tspan class="f-lav">SAM ROWE</tspan> <tspan class="f-teal">LEO BRIGHTWATER</tspan></text>
      <text x="0" y="190" textLength="698" lengthAdjust="spacingAndGlyphs"><tspan class="f-sky">RAVI MEHTA</tspan> <tspan class="f-lav">TESSA OKAFOR</tspan></text>
    </svg>

    <div class="details">
      <div class="details-group">
        <span class="d-xl t-plum">HOSTED BY</span>
        <span class="d-md t-ink">DALE MARLOW</span>
      </div>
      <div class="details-group">
        <span class="d-xl t-plum">EVERY FIRST</span>
        <span class="d-lg t-ink">WEDNESDAY</span>
        <span class="d-sm t-plum">OF THE MONTH</span>
      </div>
      <div class="details-group">
        <span class="d-lg t-ink">FREE ENTRY</span>
        <span class="d-md"><span class="t-plum">OPEN</span> <span class="t-ink">630PM</span></span>
        <span class="d-xs"><span class="t-plum">NEXT SHOW</span> <span class="t-ink">JUNE 1</span></span>
      </div>
    </div>
  </article>
</body>
</html>
```